Presentation Folder for Brisk Estates

We are a new property management / real estate company in Denver Colorado and are in need of new stationary design. Attached are our business card and logo deigns. We are looking for our stationary design. We need a presentation folder design that is Professional, exciting, and approachable. We do not have a preference on folder layout (pockets, style of folding) but will most likely be using a standard two pocket folder design (roughly 9x12) but feel free to experiment with and folder style as long as we can find a place to print them. We would also like to have a matching letterhead/page design
Below is standard size of folder from lumo press
Full Bleed Size
20.87" x 16.68"
53 x 42.4 cm
6260 x 5004 pixels
Document Trim Size
20.75" x 16.56"
52.7 x 42.1 cm
6225 x 4969 pixels
Target Market(s)
We are attempting to target the top end of the real estate market in Denver Colorado. Are target market is investors in real estate.
Industry/Entity Type
Property Management
Font styles to use
Other font styles liked:
- Would like to keep font same to logo
Look and feel
Each slider illustrates characteristics of the customer's brand and the style your logo design should communicate.

```html
<!DOCTYPE html>
<html lang="en">
<head>
<meta charset="utf-8">
<title>Brisk Estates – Presentation Folder &amp; Letterhead</title>
<link rel="stylesheet" href="https://fonts.googleapis.com/css2?family=Oswald:wght@400;500&family=Open+Sans:wght@400;600&display=swap">
<style>
  :root {
    --brand-blue: #4fa2bc;
    --brand-blue-dark: #3a8aa3;
    --brand-grey: #55595c;
    --ink-soft: #8a8f93;
    --paper: #ffffff;
    --stage: #ececec;
    --dieline: #b9b9b9;
    --city-dark: #3f4244;
    --city-mid: #7d8184;
  }
  * { box-sizing: border-box; margin: 0; padding: 0; }
  html, body { width: 1200px; height: 1000px; overflow: hidden; }
  body { background: var(--stage); font-family: "Open Sans", Arial, sans-serif; color: var(--brand-grey); position: relative; }

  .panel-label { position: absolute; font-size: 14px; color: #222; }

  .folder-back {
    position: absolute; left: 40px; top: 40px; width: 290px; height: 420px;
    background: linear-gradient(160deg, var(--city-mid) 0%, var(--city-dark) 70%, #2f3234 100%);
    border: 1px solid var(--dieline);
  }
  .folder-back .wordmark { position: absolute; top: 70px; left: 0; width: 100%; text-align: center; color: var(--paper); }
  .folder-back .wordmark .name { font-size: 18px; }
  .folder-back .wordmark .tag { font-size: 6px; letter-spacing: .3px; color: #ddd; }

  .folder-front {
    position: absolute; left: 330px; top: 40px; width: 290px; height: 420px;
    background: var(--paper); border: 1px solid var(--dieline); overflow: hidden;
  }
  .folder-front .top-band { position: absolute; left: 0; top: 0; width: 100%; height: 22px; background: var(--brand-blue); }

  .wordmark { font-family: "Oswald", "Arial Narrow", sans-serif; }
  .wordmark .dot { display: inline-block; border-radius: 50%; background: var(--brand-blue); vertical-align: middle; }
  .wordmark .name { font-weight: 500; text-transform: uppercase; letter-spacing: .5px; vertical-align: middle; }

  .front-mark { position: absolute; top: 170px; left: 0; width: 100%; text-align: center; }
  .front-mark .dot { width: 34px; height: 34px; display: block; margin: 0 auto 10px; }
  .front-mark .name { font-size: 34px; color: var(--brand-blue-dark); line-height: 1; }
  .front-mark .tag { font-family: "Open Sans", Arial, sans-serif; font-size: 10px; color: var(--brand-grey); margin-top: 4px; }
  .front-web { position: absolute; bottom: 28px; width: 100%; text-align: center; font-size: 10px; color: var(--brand-grey); }

  .pockets { position: absolute; left: 40px; top: 460px; }
  .pocket-label { font-size: 14px; fill: #222; font-family: "Open Sans", Arial, sans-serif; }

  .card-slot {
    position: absolute; left: 440px; top: 490px; width: 120px; height: 68px;
    background: var(--paper); border: 1px solid #ccc; padding: 8px 10px; font-size: 6px; line-height: 1.5; color: var(--brand-grey);
  }
  .card-slot .card-name { font-weight: 600; }

  .pocket-mark { position: absolute; left: 150px; top: 480px; transform: rotate(180deg); color: var(--brand-grey); }
  .pocket-mark .name { font-size: 20px; }
  .pocket-mark .dot { width: 16px; height: 16px; margin-right: 6px; }

  .letterhead {
    position: absolute; left: 680px; top: 140px; width: 480px; height: 621px;
    background: var(--paper); box-shadow: 0 6px 22px rgba(0,0,0,.18); overflow: hidden;
  }
  .letterhead .head { position: absolute; left: 36px; top: 30px; color: var(--brand-blue-dark); }
  .letterhead .head .dot { width: 16px; height: 16px; margin-right: 6px; }
  .letterhead .head .name { font-size: 16px; }
  .letterhead .side-band { position: absolute; left: 0; top: 0; width: 6px; height: 100%; background: var(--brand-blue); opacity: .55; }
  .letterhead .contacts { position: absolute; left: 36px; bottom: 40px; font-size: 9px; line-height: 1.7; color: var(--brand-grey); list-style: none; }
  .letterhead .contacts li::before { content: ""; display: inline-block; width: 6px; height: 6px; background: var(--brand-blue); margin-right: 6px; vertical-align: middle; }
  .letterhead .vertical-web {
    position: absolute; right: 14px; bottom: 160px; font-size: 8px; color: var(--ink-soft);
    transform: rotate(-90deg); transform-origin: right bottom; white-space: nowrap;
  }
</style>
</head>
<body>
  <span class="panel-label" style="left:165px; top:14px;">Back</span>
  <span class="panel-label" style="left:455px; top:14px;">Front</span>

  <section class="folder-back" role="img" aria-label="Wireframe city street scene with towers and pedestrians in grey with blue accents">
    <div class="wordmark">
      <div class="name">Brisk Estates</div>
      <div class="tag">Property Management and Real Estate</div>
    </div>
  </section>

  <section class="folder-front">
    <div class="top-band"></div>
    <div class="wordmark front-mark">
      <span class="dot"></span>
      <div class="name">Brisk Estates</div>
      <div class="tag">Property Management and Real Estate</div>
    </div>
    <div class="front-web">www.briskestatesco.com</div>
  </section>

  <svg class="pockets" width="580" height="460" viewBox="0 0 580 460" aria-hidden="true">
    <polygon points="0,20 20,0 20,440 0,420" fill="#fff" stroke="#b9b9b9"/>
    <polygon points="20,0 290,0 20,440" fill="#fff" stroke="#b9b9b9"/>
    <polygon points="20,300 100,300 20,440" fill="var(--brand-blue)"/>
    <polygon points="290,0 560,0 560,440" fill="#fff" stroke="#b9b9b9"/>
    <polygon points="330,65 560,65 560,440" fill="var(--brand-blue)"/>
    <polygon points="560,0 580,20 580,420 560,440" fill="#fff" stroke="#b9b9b9"/>
    <text class="pocket-label" x="130" y="245">pocket</text>
    <text class="pocket-label" x="330" y="245">pocket</text>
  </svg>

  <div class="wordmark pocket-mark"><span class="dot"></span><span class="name">Brisk Estates</span></div>

  <div class="card-slot">
    <div class="card-name">Avery Lane</div>
    <div>Managing Broker</div>
    <div>303 555 0188</div>
    <div>Denver, CO</div>
  </div>

  <section class="letterhead">
    <div class="side-band"></div>
    <div class="wordmark head"><span class="dot"></span><span class="name">Brisk Estates</span></div>
    <ul class="contacts">
      <li>303 555 0147</li>
      <li>(720) 555 0139</li>
      <li>(720) 555 0162</li>
      <li>hello@briskestatesco.com</li>
    </ul>
    <div class="vertical-web">www.briskestatesco.com</div>
  </section>
</body>
</html>
```